Technical product manual needs upgrade

For a US-based company called TRV Fixings, Inc (www.trv-fixings.example) we need to make our product manual more attractive. The product described in the manual is a metal clamp used for mounting cylinder-shaped industrial parts. All the information is already there, but it misses attractiveness, lacks company identity and perhaps the information should be rearranged to make it easier to understand. The print would be on one-sided A3 size paper. The final design should incorporate our company colors / logo / identity (though not too much) and communicate a sense of industrial reliability and attention for detail. However, the design should be easy to understand and not distract from the end goal of being a product manual.

Target Market(s)

Installation engineers / service engineers / purchasers

Industry/Entity Type

It Company

Font styles to use
Serif
Sans Serif

Colors

Designer to choose colors to be used in the design.

Requirements
Must have
• Easy to understand structure / arrangement of information
• Professional / reliable look
• Company colors but not too much since it is a manual that will be printed
• #1abc9c
• #193441
• Company logo
Nice to have
• #ecab18
Should not have
• A backside (project is one-sided paper)
• Should not be 'over the top'

```html
<!DOCTYPE html>
<html lang="en">
<head>
<meta charset="utf-8">
<title>TRV Fixings – Technical Product Manual</title>
<link href="https://fonts.googleapis.com/css2?family=Open+Sans:wght@400;600;700&family=Oswald:wght@500&display=swap" rel="stylesheet">
<style>
:root{
  --navy:#193441;
  --teal:#1abc9c;
  --amber:#ecab18;
  --ink:#2a2f33;
  --muted:#5b6770;
  --paper:#ffffff;
  --stage:#f2f3f4;
  --footer:#b9c6d1;
  --line:#c7ccd1;
  --art:#e4e7ea;
}
*{box-sizing:border-box;margin:0;padding:0}
html,body{width:1200px;height:883px;overflow:hidden;background:var(--stage)}
body{font-family:"Open Sans",Arial,sans-serif;color:var(--ink)}
.sheet{position:absolute;left:40px;top:46px;width:1120px;height:792px;background:var(--paper);box-shadow:0 4px 18px rgba(0,0,0,.12);display:flex;flex-direction:column}
.masthead{height:112px;background:var(--navy);border-bottom:5px solid var(--teal);display:flex;align-items:center;padding:0 34px;color:#fff}
.contact{width:330px;font-size:10.5px;line-height:1.45}
.contact strong{font-size:12px;font-weight:700;display:block}
.contact .label{color:var(--teal)}
.title{flex:1;text-align:center;font-family:"Oswald",Arial,sans-serif;font-weight:500;font-size:34px;line-height:1.02;letter-spacing:.5px;text-transform:uppercase}
.brand{width:330px;display:flex;justify-content:flex-end;align-items:center;gap:10px;font-size:24px;font-weight:700;letter-spacing:.5px}
.brand-dot{width:16px;height:16px;border-radius:50%;background:var(--teal)}
.columns{flex:1;display:flex;padding:18px 26px 14px}
.col{flex:1;padding:0 18px}
.col+.col{border-left:2px dotted var(--line)}
h2{font-size:14px;font-weight:700;text-transform:uppercase;color:var(--navy);line-height:1.15;margin-bottom:8px}
.col-parts h2{text-align:center}
.art{background:var(--art);border-radius:4px}
.parts-art{height:170px;margin-bottom:12px}
.parts-table{width:100%;border-collapse:collapse;font-size:9.5px}
.parts-table caption{background:var(--teal);color:#fff;font-weight:700;font-size:10.5px;padding:4px;text-transform:uppercase}
.parts-table th{background:var(--teal);color:#fff;font-weight:600;padding:3px;border:1px solid #fff}
.parts-table td{border-bottom:1px solid var(--line);padding:4px;vertical-align:middle}
.parts-table td:nth-child(-n+2){text-align:center}
.lists{display:flex;gap:18px;margin-top:16px}
.lists h3{font-size:11.5px;font-weight:700;text-transform:uppercase;color:var(--navy);margin-bottom:4px;line-height:1.15}
.lists ul{list-style:none;font-size:10.5px;line-height:1.4}
.intro{font-size:10px;line-height:1.45;color:var(--muted);margin-bottom:12px}
.steps{display:grid;grid-template-columns:repeat(3,1fr);gap:12px 10px}
.step{position:relative;height:86px}
.step-tag{position:absolute;top:4px;right:4px;width:18px;height:18px;border:1px solid var(--navy);border-radius:50%;background:#fff;font-size:9px;font-weight:700;display:flex;align-items:center;justify-content:center;color:var(--navy)}
.col-instructions h2{text-align:center}
.col-instructions h4{color:var(--amber);font-size:11px;font-weight:700;margin:10px 0 3px}
.col-instructions p,.col-instructions ol{font-size:9.6px;line-height:1.5}
.col-instructions ol{padding-left:14px}
.disclaimer{height:74px;background:var(--footer);padding:14px 40px;font-size:10.5px;line-height:1.5;color:var(--navy);display:flex;align-items:center}
</style>
</head>
<body>
<main class="sheet">
  <header class="masthead">
    <div class="contact">
      <strong>TRV Fixings, Inc.</strong>
      1840 Harbor Park Dr Suite 210 Dayton, OH 45402<br>
      <span class="label">E:</span> info@trv-fixings.example<br>
      <span class="label">T:</span> 1-555-014-2290
    </div>
    <h1 class="title">Technical<br>Product Manual</h1>
    <div class="brand"><span class="brand-dot"></span>TRV Fixings</div>
  </header>

  <section class="columns">
    <div class="col col-parts">
      <h2>Parts</h2>
      <div class="art parts-art" role="img" aria-label="Exploded technical drawing of the clamp with numbered callouts 1 to 5"></div>
      <table class="parts-table">
        <caption>Parts list &nbsp;&nbsp; 1 camp</caption>
        <thead><tr><th>Item</th><th>Qty</th><th>Description</th><th>Material</th></tr></thead>
        <tbody>
          <tr><td>1</td><td>1</td><td>Clamp body single bolt</td><td>Steel Zn plated</td></tr>
          <tr><td>2</td><td>1</td><td>Hex cap screw 7/16x3.25</td><td>Zinc plated, steel, mild</td></tr>
          <tr><td>3</td><td>1</td><td>Hex nuts 7/16</td><td>Zinc plated, steel, mild</td></tr>
          <tr><td>4</td><td>2</td><td>Upper protection rubber</td><td>EPDM rubbershore hardness 65° ±5°</td></tr>
          <tr><td>5</td><td>2</td><td>Lower protection rubber</td><td>EPDM rubbershore hardness 65° ±5°</td></tr>
        </tbody>
      </table>
      <div class="lists">
        <div><h3>Required tooling</h3><ul><li>Spanner</li><li>Torque wrench</li><li>Level tool</li></ul></div>
        <div><h3>Recommended protection measures</h3><ul><li>Safety gloves</li><li>Safety goggles</li></ul></div>
      </div>
    </div>

    <div class="col col-assembly">
      <h2>Accumulator assembly recommendations</h2>
      <p class="intro">For the positioning and assembly of any hydraulic accumulator above 50 Lbs. we advise to always use an accumulator lifting cap. Please refer to your accumulator supplier for this.</p>
      <div class="steps">
        <div class="art step" role="img" aria-label="Assembly drawing A"><span class="step-tag">A</span></div>
        <div class="art step" role="img" aria-label="Assembly drawing B"><span class="step-tag">B</span></div>
        <div class="art step" role="img" aria-label="Assembly drawing C"><span class="step-tag">C</span></div>
        <div class="art step" role="img" aria-label="Assembly drawing D"><span class="step-tag">D</span></div>
        <div class="art step" role="img" aria-label="Assembly drawing E"><span class="step-tag">E</span></div>
        <div class="art step" role="img" aria-label="Assembly drawing F"><span class="step-tag">F</span></div>
        <div class="art step" role="img" aria-label="Assembly drawing G"><span class="step-tag">G</span></div>
        <div class="art step" role="img" aria-label="Assembly drawing H"><span class="step-tag">H</span></div>
        <div class="art step" role="img" aria-label="Assembly drawing I"><span class="step-tag">I</span></div>
        <div class="art step" role="img" aria-label="Assembly drawing J"><span class="step-tag">J</span></div>
        <div class="art step" role="img" aria-label="Assembly drawing K"><span class="step-tag">K</span></div>
        <div class="art step" role="img" aria-label="Assembly drawing L"><span class="step-tag">L</span></div>
      </div>
    </div>

    <div class="col col-instructions">
      <h2>Instructions</h2>
      <h4>Assembly of rubber onto clamp</h4>
      <p>We advise you to use safety gloves for the assembly of the clamp.</p>
      <ol>
        <li>Place lower protection rubbers (item no. 5) on to the inside of the lower clamp half and fold edges of the rubber over the clamp band, as shown in images A, B, C and D.</li>
        <li>Place upper protection rubbers (item no. 4) on to the inside of the upper clamp half and fold edges of the rubber over the clamp band, as shown in images E, F, G and H.</li>
      </ol>
      <h4>Mounting of clamp onto wall / frame / etc.</h4>
      <p>We recommend you to mount your clamp onto a stable surface and to always use a levelling tool. The mounting materials used should be in accordance with the mounting holes already present on the clamp. The mounting holes are located on the bottom of the mounting part of the clamp and are NOT the same holes as the holes for the hex cap screw.</p>
      <h4>Positioning of accumulator</h4>
      <p>Position your accumulator into the open clamp(s) as described by your accumulator supplier.</p>
      <h4>Tightening hex cap screw and closing clamp</h4>
      <p>Adjust your torque wrench to the advised torque level of 35nm.</p>
      <ol>
        <li>Place the hex cap screw (item no. 2) fully through the bolt holes until the cap (head) of the screw touches the spacer, as shown in images I and J.</li>
        <li>Place the hex nut (item no. 3) on the end of the hex cap screw, as shown in images K and L.</li>
        <li>Place the spanner on the bolt head.</li>
        <li>Place the torque wrench on the hex nut.</li>
        <li>Hold the spanner steady and use the torque wrench to reach the advised torque level.</li>
        <li>Check if accumulator is mounted securely.</li>
      </ol>
    </div>
  </section>

  <footer class="disclaimer">
    <p>The sole purpose of this product manual is to provide instructions for mounting the accumulator clamps as supplied by TRV Fixings, Inc. Please keep in mind that TRV Fixings, Inc. manufactures nor sells accumulators and is in no way liable for any damage or injury involving the handling, moving or mounting of accumulators itself.</p>
  </footer>
</main>
</body>
</html>
```